Garage Door Sales and Repair Website

Looking for a website theme and home page design for a garage door sales and repair company (Copper Ridge Garage).   We have a new logo and color scheme (attached) and need to update our website to match.  Here is the current site http://www.copperridgegarage.example/
The design should lend it self to being responsive and full screen.
I like this site (http://www.bluefern-site-works.example/) how it has different color blocks and I would like to have a slide show on my home page as well.  4 slides utilizing some of the following concepts Garage Opener, Garage Doors, Springs, Garage Door Repair, Specials, Free Estimate, etc...
Would like color design to match logo / business cards attached.
Call for Free Estimate with phone number should be visible on top of the page as well.

Target Market(s)
Consumers
Industry/Entity Type
Professional Service
Number of Pages Required
1 page
Font styles to use
Other font styles liked:
- Oswald, Open Sans, other similar google web fonts

Requirements
Must have
- 4 slides for home page design
- Free Estimate
- Phone Number

Nice to have
- Call out for online specials

```html
<!DOCTYPE html>
<html lang="en">
<head>
<meta charset="utf-8">
<title>Copper Ridge Garage – Home</title>
<link rel="stylesheet" href="https://fonts.googleapis.com/css2?family=Open+Sans:wght@400;600;700&display=swap">
<style>
:root{
  --navy:#4a5578;
  --navy-deep:#3d4a72;
  --band:#46527a;
  --ink:#555;
  --light:#f2f2f2;
  --footer:#7a7a7a;
  --scroll:#d3d3d3;
  --white:#fff;
}
*{box-sizing:border-box;margin:0;padding:0}
html,body{width:1200px;height:1200px;overflow:hidden;background:var(--white);font-family:'Open Sans',sans-serif}
.page{position:absolute;left:283px;top:0;width:760px;height:1500px;transform:scale(.8);transform-origin:0 0;background:var(--white)}
.abs{position:absolute}
/* header */
.site-header{left:0;top:0;width:760px;height:49px;background:var(--navy)}
.brand{left:48px;top:12px;display:flex;align-items:center;gap:5px;color:var(--white);font-size:8px;font-weight:700;line-height:1.1;width:70px}
.brand i{width:12px;height:12px;border-radius:50%;background:var(--white);flex:none}
.nav{left:150px;top:17px;display:flex;gap:20px;font-size:8px;font-weight:700;color:var(--white)}
.nav span:first-child{color:#c9cde0}
.search{left:566px;top:14px;width:150px;height:19px;background:var(--white);border:1px solid #ccc;font-size:8px;color:#999;padding:4px 10px}
.search svg{position:absolute;right:0;top:-1px}
/* hero */
.hero{left:0;top:49px;width:760px;height:256px;overflow:hidden}
.hero-photo{left:0;top:0;width:760px;height:256px;background:linear-gradient(100deg,#fdfdfd 0%,#e4e4e6 35%,#b7404d 50%,#8d3d52 60%,#5e6382 75%,#5a6282 100%)}
.hero-title{left:401px;top:12px;font-size:27px;font-weight:400;line-height:34px;white-space:nowrap;color:var(--white);letter-spacing:-.2px}
.hero-copy{left:404px;top:50px;width:225px;font-size:11px;line-height:15.5px;color:var(--white)}
.hero-contact{left:431px;top:138px;font-size:17px;font-weight:600;color:var(--white)}
.hero-line{left:451px;font-size:12.5px;font-weight:600;color:var(--white);display:flex;align-items:center;gap:7px;white-space:nowrap}
.badge-plain{left:468px;top:219px;width:74px;height:28px;background:#111;border-radius:2px}
.badge-round{left:570px;top:217px;width:26px;height:26px;border-radius:50%;background:#e5b53a}
.badge-award{left:648px;top:78px;width:96px;height:96px;border-radius:50%;border:3px solid #ddd;background:rgba(255,255,255,.15)}
.dots{left:337px;top:237px;width:83px;height:19px;background:var(--white);display:flex;justify-content:center;align-items:center;gap:12px}
.dots i{width:6px;height:6px;border-radius:50%;background:var(--navy)}
.dots i:nth-child(2){background:none;border:1.5px solid var(--navy)}
/* services */
.section-title{width:760px;text-align:center;color:var(--navy);font-size:15px;font-weight:400}
.service{width:175px;text-align:center}
.service .photo{width:129px;height:105px;margin:0 auto}
.service h3{margin-top:14px;font-size:9.5px;font-weight:600;color:var(--navy)}
.service p{margin:8px auto 0;width:150px;font-size:8.5px;line-height:10.6px;color:var(--ink)}
/* specials */
.specials{left:0;top:644px;width:760px;height:270px;background:var(--band);color:var(--white);text-align:center}
.specials h2{position:absolute;top:14px;width:100%;font-size:16px;font-weight:600}
.specials .sub{position:absolute;top:41px;width:100%;font-size:10.5px}
.specials .sub2{position:absolute;top:59px;width:100%;font-size:8.5px}
.coupon{position:absolute;border:2px solid var(--white);border-radius:3px;padding-top:2px}
.coupon b{display:block;font-size:17px;font-weight:400;line-height:20px}
.coupon span{display:block;font-size:14.5px;line-height:18px}
.coupon small{display:block;font-size:6.5px;margin-top:2px}
.specials .note{position:absolute;top:248px;width:100%;font-size:8.5px}
/* estimate */
.estimate{left:0;top:914px;width:760px;height:211px;background:var(--light)}
.label{font-size:10px;color:var(--navy)}
.field{background:var(--white);border:1px solid #bbb;font-size:7.5px;color:#999;padding:4px 8px;height:19px}
.submit{left:408px;top:142px;width:87px;height:20px;background:var(--navy-deep);color:var(--white);font-size:11px;font-weight:700;text-align:center;line-height:20px}
.callout{left:560px;top:124px;width:122px;text-align:center;color:var(--navy)}
.callout small{display:block;font-size:9px;margin-top:28px}
.callout b{display:block;font-size:17px;font-weight:700;line-height:18px;border-top:1px solid var(--navy);border-bottom:1px solid var(--navy)}
.privacy{width:760px;text-align:center;color:var(--navy)}
/* footer */
.footer{left:0;top:1125px;width:760px;height:375px;background:var(--footer);color:var(--white)}
.foot-brand{left:42px;top:20px;width:114px;height:100px;display:flex;flex-direction:column;align-items:center;justify-content:center;gap:6px;font-size:15px;font-weight:700;text-align:center;line-height:17px}
.foot-brand i{width:22px;height:22px;border-radius:50%;background:var(--white)}
.col-head{font-size:12px;text-align:center;padding-bottom:3px;border-bottom:2px solid var(--white)}
.col-body{font-size:10px;line-height:12.5px;white-space:nowrap}
.social-row{display:flex;align-items:center;gap:8px;font-size:11px;height:25px}
.social-row i{width:17px;height:17px;background:#5a6a99;display:block}
.copyright{left:0;top:132px;width:760px;text-align:center;font-size:7px}
.scroll-bar{left:0;top:152px;width:760px;height:28px;background:var(--scroll);text-align:center;font-size:10.5px;line-height:28px;color:var(--white);letter-spacing:.3px}
.products-title{left:0;top:202px;width:760px;text-align:center;font-size:11.5px;font-weight:600}
.products{left:46px;top:231px;width:670px;height:108px;border:2px solid #ccc;background:#9b9b9b}
.product{position:absolute;font-size:6.5px;font-weight:700;display:flex;align-items:center;gap:4px;white-space:nowrap}
.product i{width:7px;height:7px;background:var(--white);position:relative;flex:none}
.product i::after{content:"";position:absolute;left:2px;top:0;width:2px;height:4px;border:solid #555;border-width:0 1.3px 1.3px 0;transform:rotate(45deg)}
</style>
</head>
<body>
<div class="page">
  <header class="abs site-header">
    <div class="abs brand"><i></i>Copper Ridge Garage</div>
    <nav class="abs nav"><span>HOME</span><span>OPENERS</span><span>GARAGE DOORS</span><span>BROKEN SPRINGS</span><span>GARAGE DOOR REPAIR</span><span>BLOG</span></nav>
    <div class="abs search">Search
      <svg width="21" height="19" viewBox="0 0 21 19"><rect width="21" height="19" fill="#fff" stroke="#ccc"/><circle cx="9.5" cy="8.5" r="4" fill="none" stroke="#4a5578" stroke-width="2"/><line x1="12.5" y1="11.5" x2="16" y2="15" stroke="#4a5578" stroke-width="2"/></svg>
    </div>
  </header>

  <section class="abs hero">
    <div class="abs hero-photo" role="img" aria-label="Close-up of a white garage door opener unit with red branded cover"></div>
    <h1 class="abs hero-title">GARAGE DOOR OPEANER</h1>
    <p class="abs hero-copy">We offer Garage door opeaners from top manufacturers like Hoistline, Vantor, Raylock, Castellan, Benchwright and more.</p>
    <div class="abs hero-contact">CONTACT US</div>
    <div class="abs hero-line" style="top:170px">
      <svg width="14" height="14" viewBox="0 0 14 14"><path d="M3 1l2.5 3-1.5 1.5c1 2 2.5 3.5 4.5 4.5L10 8.5l3 2.5-1.5 2C6.5 13 1 7.5 1 2.5z" fill="none" stroke="#fff" stroke-width="1.2"/></svg>555-014-2290</div>
    <div class="abs hero-line" style="top:195px">
      <svg width="15" height="11" viewBox="0 0 15 11"><rect x="1" y="1" width="13" height="9" fill="none" stroke="#fff" stroke-width="1.2"/><path d="M1 1l6.5 5L14 1" fill="none" stroke="#fff" stroke-width="1.2"/></svg>info@copperridgegarage.example</div>
    <div class="abs badge-plain"></div>
    <div class="abs badge-round"></div>
    <div class="abs badge-award"></div>
    <div class="abs dots"><i></i><i></i><i></i><i></i></div>
  </section>

  <h2 class="abs section-title" style="top:332px">SERVICES</h2>
  <div class="abs service" style="left:31px;top:378px">
    <div class="photo" role="img" aria-label="Technician on a ladder repairing a garage door track" style="background:linear-gradient(160deg,#8a5a3c,#c8b39a 55%,#3f4a66);border-radius:60px 0 0 0"></div>
    <h3>GARAGE DOOR REPAIR</h3>
    <p>Copper Ridge Garage offers complete garage door repair and door maintenance services. Damaged panels, bent tracks, damaged rollers, broken springs, worn weather seal. Whatever the problem, Copper Ridge Garage can fix it!</p>
  </div>
  <div class="abs service" style="left:206px;top:378px">
    <div class="photo" role="img" aria-label="Garage door opener unit with keypad and remote" style="background:linear-gradient(150deg,#e8e8e8,#c9c9c9 50%,#b23a3a 70%,#9a9a9a)"></div>
    <h3>GARAGE DOOR OPENERS</h3>
    <p>Copper Ridge Garage offers a complete line of Garage Door Openers and accessories, from top manufacturers like Hoistline, Vantor, Raylock, Castellan, Benchwright and more. Whether you're replacing an old, worn out model, or installing a new opener for the first time, we have an opener to suit your needs!</p>
  </div>
  <div class="abs service" style="left:380px;top:378px">
    <div class="photo" role="img" aria-label="House with a new wooden double garage door" style="background:linear-gradient(180deg,#b9c3cc 0%,#6f6a5c 35%,#7a3a24 65%,#8d8a80 100%)"></div>
    <h3>NEW GARAGE DOORS</h3>
    <p>Copper Ridge Garage installs new garage doors. We will come to your home, take measurements, discuss your options with you, and give you a free estimate for a new garage door. We will help you select the perfect door for your home.</p>
  </div>
  <div class="abs service" style="left:555px;top:378px">
    <div class="photo" role="img" aria-label="Close-up of a rusty broken torsion spring" style="background:linear-gradient(180deg,#3a2a20,#8a5a3a 45%,#5a4a40 70%,#b0a8a0);border-radius:0 60px 0 0"></div>
    <h3>BROKEN SPRINGS</h3>
    <p>Copper Ridge Garage is your local garage door spring replacement expert! We replace broken torsion springs, extension springs, and torque-master springs, on residential doors and most commercial and industrial doors as well.</p>
  </div>

  <section class="abs specials">
    <h2>SPECIALS</h2>
    <div class="sub">SAME DAY GARAGE DOOR REPAIR &amp; SERVICE</div>
    <div class="sub2">FAST – AFFORDABLE – PROFESSIONAL – NO ADDITIONAL CHARGE FOR WEEKENDS – 24 HOUR EMERGENCY SERVICE AVAILABLE</div>
    <div class="coupon" style="left:68px;top:88px;width:278px;height:61px"><b>$60 OFF</b><span>SPRING REPLACEMENT</span><small>$60 OFF REPLACEMENT OF TWO GARAGE DOOR SPRINGS</small></div>
    <div class="coupon" style="left:393px;top:88px;width:271px;height:61px"><b>$100 OFF</b><span>NEW GARAGE DOOR</span><small>PURCHASE AND INSTALLATION OF ANY SINGLE DOOR</small></div>
    <div class="coupon" style="left:70px;top:171px;width:274px;height:61px"><b>$60 OFF</b><span>NEW GARAGE DOOR</span><small>$200 OFF PURCHASE AND INSTALLATION OF ANY DOUBLE DOOR</small></div>
    <div class="coupon" style="left:393px;top:171px;width:272px;height:61px"><b>$60 OFF</b><span>SPRING REPLACEMENT</span><small>OVERHAUL INCLUDES NEW SPRINGS, ROLLERS, CABLES, PULLEYS &amp; BEARINGS</small></div>
    <div class="note">*** Must present / mention coupon at time of estimate. Not valid with other offers</div>
  </section>

  <section class="abs estimate">
    <h2 class="abs section-title" style="top:8px">SCHEDULE FREE ESTIMATE</h2>
    <div class="abs label" style="left:78px;top:42px">Name</div>
    <div class="abs label" style="left:78px;top:73px">Email</div>
    <div class="abs label" style="left:78px;top:104px">Phone Number</div>
    <div class="abs field" style="left:164px;top:39px;width:186px">Your Name</div>
    <div class="abs field" style="left:164px;top:71px;width:186px">Your Email</div>
    <div class="abs field" style="left:164px;top:103px;width:186px">Phone Number</div>
    <div class="abs label" style="left:388px;top:42px">Type Of Estimate</div>
    <div class="abs label" style="left:388px;top:73px">Other Information</div>
    <div class="abs field" style="left:496px;top:39px;width:186px;color:#444">Garage Door Repair
      <svg class="abs" style="right:6px;top:7px" width="7" height="5"><path d="M0 0h7L3.5 5z" fill="#888"/></svg></div>
    <div class="abs field" style="left:496px;top:71px;width:186px;height:49px"></div>
    <div class="abs label" style="left:157px;top:145px">Preferred Date <span style="font-size:7.5px">(Optional)</span></div>
    <div class="abs field" style="left:277px;top:143px;width:75px;color:#444">05/11/2016
      <svg class="abs" style="right:4px;top:4px" width="11" height="10"><rect x=".5" y="1.5" width="10" height="8" fill="none" stroke="#4a5578"/><line x1="0" y1="4" x2="11" y2="4" stroke="#4a5578"/></svg></div>
    <div class="abs submit">SUBMIT</div>
    <div class="abs callout">
      <svg class="abs" style="left:22px;top:0" width="78" height="30"><path d="M2 30a37 30 0 0 1 74 0" fill="none" stroke="#4a5578" stroke-width="2"/></svg>
      <small>Call for a FREE Estimate</small><b>555-014-2290</b>
    </div>
    <div class="abs privacy" style="top:180px;font-size:9px">Your information is safe with us!</div>
    <div class="abs privacy" style="top:194px;font-size:7px">We understand the importance of privacy, because of that we will NEVER sell you information to a third party</div>
  </section>

  <footer class="abs footer">
    <div class="abs foot-brand"><i></i>Copper Ridge Garage</div>
    <div class="abs" style="left:193px;top:10px;width:181px">
      <div class="col-head">CONTACT</div>
      <div class="col-body" style="margin-top:9px">Copper Ridge Garage,<br>Alder Blvd,<br>Lakeview, CO 80990.</div>
      <div class="col-body" style="margin-top:8px"><b>CALL US :</b>&nbsp;&nbsp; 555-014-2290</div>
      <div class="col-body" style="margin-top:7px;font-size:8.5px"><b>EAMIL US :</b> info@copperridgegarage.example</div>
    </div>
    <div class="abs" style="left:407px;top:10px;width:126px">
      <div class="col-head">NAVIGATION</div>
      <div class="col-body" style="margin-top:9px;font-size:8.5px">Home<br>Openers<br>Garage Doors<br>Broken Springs<br>Garage Door Repair<br>Blog</div>
    </div>
    <div class="abs" style="left:570px;top:10px;width:148px">
      <div class="col-head">SOCAL NETWORK</div>
      <div style="margin-top:4px">
        <div class="social-row"><i></i>Friendbook</div>
        <div class="social-row"><i></i>ProLink</div>
        <div class="social-row"><i></i>Chirper</div>
      </div>
    </div>
    <div class="abs copyright">Copyright © 2008 - 2016 Copper Ridge Garage Sales &amp; Repair, LLC. All rights reserved. Powered by <u>Northpeak Media</u></div>
    <div class="abs scroll-bar">SCROLL DOWN TO VIEW ALL SERVICES
      <svg style="vertical-align:middle;margin-left:14px" width="12" height="16"><path d="M6 0v13M1 8l5 6 5-6" fill="none" stroke="#fff" stroke-width="2"/></svg></div>
    <div class="abs products-title">Garage Door Products &amp; Services</div>
    <div class="abs products">
      <div class="product" style="left:9px;top:14px"><i></i>Garage Door Repair</div>
      <div class="product" style="left:129px;top:14px"><i></i>New Garage Doors</div>
      <div class="product" style="left:249px;top:14px"><i></i>Garage Door Openers</div>
      <div class="product" style="left:389px;top:14px"><i></i>Garage Door Maintenance</div>
      <div class="product" style="left:529px;top:14px"><i></i>Garage Door Tune and Lube</div>
      <div class="product" style="left:9px;top:35px"><i></i>Broken Springs</div>
      <div class="product" style="left:129px;top:35px"><i></i>New Springs</div>
      <div class="product" style="left:249px;top:35px"><i></i>Broken or Frayed Cables</div>
      <div class="product" style="left:389px;top:35px"><i></i>Stuck / Off-Track Doors</div>
      <div class="product" style="left:529px;top:35px"><i></i>Damaged Tracks &amp; Rollers</div>
      <div class="product" style="left:9px;top:56px"><i></i>Warped Garage Doors</div>
      <div class="product" style="left:129px;top:56px"><i></i>Bent Garage Doors</div>
      <div class="product" style="left:249px;top:56px"><i></i>Wind Damaged Garage Doors</div>
      <div class="product" style="left:389px;top:56px"><i></i>Garage Door Maintenance</div>
      <div class="product" style="left:529px;top:56px"><i></i>Garage Door Hinges</div>
      <div class="product" style="left:9px;top:77px"><i></i>Panel / Section Replacement</div>
      <div class="product" style="left:129px;top:77px"><i></i>Garage Door Opener Install</div>
      <div class="product" style="left:249px;top:77px"><i></i>Garage Door Installation</div>
      <div class="product" style="left:389px;top:77px"><i></i>Roller Replacement</div>
      <div class="product" style="left:529px;top:77px"><i></i>Garage Door Opener Remotes</div>
    </div>
  </footer>
</div>
</body>
</html>
```